Logistics Website Design

See website https://tvarfreightglobal.com for theme and color details. Need the site to be re-done and reflect some of the designs shown in this list here: https://pinvora.com/tags/logistics-company-website

Target Market(s)

Logistics & Transportation

Industry/Entity Type

Logistics and Supply Chain

Coding

Coded - Design and coding required

Number of Pages Required

5+ page

Requirements
Must have
• Colors must match theme of logo. Looking for a sleek, interactive design.

```html
<!DOCTYPE html>
<html lang="en">
<head>
<meta charset="utf-8">
<title>Tvar Freight — Website Design</title>
<link href="https://fonts.googleapis.com/css2?family=Barlow:wght@400;500;600&family=Staatliches&display=swap" rel="stylesheet">
<style>
:root{
  --ink:#0a172a;
  --night:#0a0302;
  --deep:#1a0705;
  --brown:#2f1209;
  --card:#260a06;
  --orange:#e85e30;
  --peach:#f3a991;
  --blush:#fbe3db;
  --board:#cfcfcf;
  --muted:#8a5a4c;
}
*{margin:0;padding:0;box-sizing:border-box}
html,body{width:1200px;height:3410px;overflow:hidden}
body{background:var(--board);font-family:'Barlow',sans-serif;position:relative;color:var(--blush)}
.display{font-family:'Staatliches',sans-serif;font-weight:400;letter-spacing:.01em}
.abs{position:absolute}

/* style board */
.brand-mark{left:225px;top:130px;display:flex;align-items:center;gap:8px}
.brand-mark .dot{width:22px;height:22px;border-radius:50%;background:var(--orange)}
.brand-mark span{font-family:'Barlow',sans-serif;font-weight:600;font-size:17px;color:var(--orange)}
.board-label{font-size:22px;color:#111;font-weight:500}
.font-sample-a{left:476px;top:138px;font-family:'Staatliches',sans-serif;font-size:22px;color:#555}
.font-sample-b{left:476px;top:168px;font-size:18px;color:#666}
.swatch{top:136px;width:41px;height:41px;border-radius:50%}
.swatch-code{top:185px;width:60px;text-align:center;font-size:9px;color:#333}

/* site */
.site{left:245px;top:265px;width:709px;height:3046px;background:var(--night);overflow:hidden}
.hero-photo{left:0;top:0;width:709px;height:420px;background:linear-gradient(180deg,#8a4a38 0%,#9b5a44 35%,#6a3325 70%,var(--deep) 100%)}
.nav{left:0;top:0;width:709px;height:44px;border-bottom:1px solid rgba(251,227,219,.25);font-size:7px;color:var(--blush)}
.nav a{position:absolute;top:19px;color:var(--blush);text-decoration:none}
.nav .logo-name{left:325px;top:16px;font-weight:600;font-size:9px;display:flex;align-items:center;gap:4px}
.nav .logo-name i{width:8px;height:8px;border-radius:50%;background:var(--orange);display:block}
.hero-title{left:0;top:88px;width:709px;text-align:center;font-size:49px;line-height:44px;color:var(--blush)}
.hero-sub{left:0;top:187px;width:709px;text-align:center;font-size:9px;color:var(--blush)}
.btn{display:inline-block;font-family:'Staatliches',sans-serif;font-size:8px;padding:6px 10px;border-radius:4px;color:var(--blush);background:var(--orange)}
.btn.ghost{background:none}
.hero-ctas{left:0;top:211px;width:709px;text-align:center}
.below-hero{left:0;top:420px;width:709px;height:322px;background:var(--deep)}
.video-card{left:192px;top:411px;width:324px;height:90px;border-radius:6px;background:#2a0e08;border:1px solid #4a2016}
.video-card h3{position:absolute;left:18px;top:20px;font-size:16px;line-height:19px;color:var(--peach)}
.video-card .rule{position:absolute;left:18px;top:64px;width:100px;height:1px;background:#5a2a1c}
.video-thumb{position:absolute;right:8px;top:6px;width:118px;height:76px;border-radius:4px;background:linear-gradient(135deg,#6a3a2c,#a55c44)}
.play{position:absolute;right:52px;top:30px;width:24px;height:24px;border-radius:50%;background:var(--orange)}
.eyebrow{left:0;top:549px;width:709px;text-align:center;font-size:7px;letter-spacing:.05em;color:var(--peach)}
.about-text{left:150px;top:565px;width:409px;text-align:center;font-size:14px;line-height:19.5px;font-weight:500;color:var(--blush)}
.stat{top:665px;display:flex;align-items:baseline;gap:8px}
.stat b{font-family:'Staatliches',sans-serif;font-weight:400;font-size:30px;color:var(--orange);line-height:28px;height:22px;overflow:hidden}
.stat span{font-size:8px;color:var(--blush)}

.provide{left:0;top:742px;width:709px;height:410px;background:#120403}
.section-title{font-size:28px;color:var(--peach);line-height:28px}
.arrow-btn{top:794px;width:22px;height:22px;border-radius:50%;border:1px solid #5a2a1c}
.arrow-btn.on{background:var(--orange);border-color:var(--orange)}
.service-card{top:841px;width:283px;height:263px;border-radius:4px;background:var(--card);border:1px solid #3a1510;overflow:hidden}
.service-card.light{background:#e0a08a}
.service-card .art{position:absolute;left:0;top:0;width:132px;height:106px;background:linear-gradient(135deg,#8a3a22,#d8683e)}
.service-card h3{position:absolute;left:19px;top:135px;font-size:15px;color:var(--orange)}
.service-card.light h3{color:var(--brown)}
.service-card p{position:absolute;left:19px;top:158px;width:250px;font-size:7.5px;line-height:13px;color:#c8a89c}
.service-card.light p{color:#6a3325}
.tags{position:absolute;left:19px;top:210px;width:250px;display:flex;flex-wrap:wrap;gap:5px}
.tag{font-size:6.5px;padding:3px 6px;border-radius:8px;background:#3a1510;color:var(--blush)}
.light .tag{background:#c98672;color:var(--brown)}

.calc{left:0;top:1152px;width:709px;height:391px;background:#0f0302}
.calc-art{left:245px;top:1198px;width:219px;height:159px;background:linear-gradient(135deg,#f0ddd3 0%,#b9785a 50%,var(--orange) 100%);border-radius:6px}
.calc-title{left:0;top:1371px;width:709px;text-align:center;font-size:29px;color:var(--orange)}
.field-label{top:1418px;font-size:6.5px;color:var(--blush)}
.select{top:1433px;width:148px;height:28px;border-radius:4px;background:#1c0805;border:1px solid #3a1510;font-size:6.5px;color:#8a6a60;padding:10px 12px}
.select svg{position:absolute;right:10px;top:11px}
.calc-btn{left:281px;top:1469px;width:148px;height:26px;border-radius:4px;background:var(--orange);text-align:center;font-family:'Staatliches',sans-serif;font-size:8px;line-height:26px;color:var(--brown)}

.why{left:0;top:1543px;width:709px;height:364px;background:var(--night)}
.why-list{left:66px;top:1676px;width:280px;border-left:1px solid #3a1510}
.why-item{position:absolute;left:12px;font-size:8.5px;color:#6a3a2c}
.why-item.on{color:var(--orange);font-weight:600}
.why-item.on p{font-weight:400;color:var(--blush);font-size:7px;line-height:12px;margin-top:4px;width:260px}
.why-photo{left:380px;top:1597px;width:262px;height:261px;border-radius:4px;background:linear-gradient(90deg,#c77a5e 0%,#3a1a14 30%,#2a1410 40%,#7a3320 55%,#3a1a14 70%,#c38068 100%)}

.reviews{left:0;top:1907px;width:709px;height:309px;background:radial-gradient(ellipse at 85% 110%,#7a3a28 0%,#3a1510 40%,var(--deep) 75%)}
.review{top:2003px;width:187px;height:163px;border-radius:4px;background:#1a0604;border:1px solid #3a1510}
.review .quote{position:absolute;left:14px;top:16px}
.review .avatar{position:absolute;right:0;top:0;width:38px;height:38px;background:linear-gradient(135deg,#8a8f98,#d8d8d8)}
.review p{position:absolute;left:14px;top:55px;width:160px;font-size:9px;line-height:14.5px;color:var(--blush)}
.review small{position:absolute;left:14px;top:140px;font-size:5.5px;color:#a88a80;font-family:'Staatliches',sans-serif}

.faq-title{left:0;top:2259px;width:709px;text-align:center;font-size:29px;color:var(--orange)}
.faq{left:171px;width:367px;border-radius:3px;background:#1a0604;border:1px solid #3a1510}
.faq h4{position:absolute;left:14px;font-family:'Staatliches',sans-serif;font-weight:400;font-size:10px;color:var(--blush);top:15px}
.faq.open{background:#1f0705}
.faq.open h4{color:var(--orange)}
.faq .toggle{position:absolute;right:14px;top:13px;width:15px;height:15px;border-radius:50%;background:var(--blush)}
.faq.open .toggle{background:var(--orange)}
.faq .answer{position:absolute;left:14px;top:46px;width:340px;font-size:7px;line-height:12px;color:var(--blush)}
.faq-more{left:0;top:2583px;width:709px;text-align:center;font-size:7px;color:#a88a80}

.cta{left:17px;top:2637px;width:674px;height:168px;border-radius:4px;background:#e09e88}
.cta h2{position:absolute;left:49px;top:54px;font-size:23px;line-height:26px;color:var(--brown);white-space:nowrap}
.cta-art{left:362px;top:2712px;width:122px;height:120px;border-radius:6px;background:linear-gradient(135deg,#b8502c,#e07048 60%,#c98a70)}
.cta .btn{position:absolute;left:480px;top:84px;z-index:2}
.cta .ghost{left:552px;color:var(--orange)}

.footer-blurb{left:66px;top:2867px;width:220px;font-size:8px;line-height:13px;font-weight:600;color:var(--blush)}
.footer-contact{left:66px;top:2904px;font-size:7px;line-height:17px;color:var(--blush)}
.footer-col{top:2868px;font-size:6.5px;line-height:16.5px;color:var(--blush)}
.footer-col h5{font-family:'Staatliches',sans-serif;font-weight:400;font-size:7px;color:var(--orange);margin-bottom:1px}
.copyright{left:397px;top:2993px;font-size:6px;color:var(--peach)}
</style>
</head>
<body>

<div class="abs brand-mark"><div class="dot"></div><span>Tvar Freight</span></div>
<div class="abs board-label" style="left:475px;top:101px">Fonts:</div>
<div class="abs font-sample-a">Staatliches</div>
<div class="abs font-sample-b">Barlow</div>
<div class="abs board-label" style="left:732px;top:101px">Colors:</div>
<div class="abs swatch" style="left:734px;background:#0a172a"></div>
<div class="abs swatch" style="left:783px;background:var(--brown)"></div>
<div class="abs swatch" style="left:833px;background:var(--orange)"></div>
<div class="abs swatch" style="left:883px;background:var(--peach)"></div>
<div class="abs swatch" style="left:934px;background:var(--blush)"></div>
<div class="abs swatch-code" style="left:724px">#0a172a</div>
<div class="abs swatch-code" style="left:773px">#2f1209</div>
<div class="abs swatch-code" style="left:823px">#e85e30</div>
<div class="abs swatch-code" style="left:873px">#f3a991</div>
<div class="abs swatch-code" style="left:924px">#fbe3db</div>

<main class="abs site">
  <div class="abs below-hero"></div>
  <div class="abs hero-photo" role="img" aria-label="Aerial photo of trucks parked at warehouse loading docks, warm copper tint"></div>
  <nav class="abs nav">
    <a style="left:66px">About Us</a>
    <a style="left:131px">Services</a>
    <a style="left:206px">Industries</a>
    <a class="logo-name"><i></i>Tvar Freight</a>
    <a style="left:475px">Fleet</a>
    <a style="left:525px">Contact Us</a>
    <a style="left:593px">Request a Quote</a>
  </nav>
  <h1 class="abs hero-title display">Delivering Strength<br>In Every Mile</h1>
  <p class="abs hero-sub">Secure &amp; reliable transportation for all your cargo needs</p>
  <div class="abs hero-ctas"><span class="btn">Request a Quote</span> <span class="btn ghost">Explore Solutions</span></div>

  <div class="abs video-card">
    <h3 class="display">The Process of Driving<br>Your Business Forward</h3>
    <div class="rule"></div>
    <div class="video-thumb" role="img" aria-label="Video still of a truck on a warm-toned road"></div>
    <div class="play"><svg width="24" height="24"><path d="M10 7 L17 12 L10 17Z" fill="#fbe3db"/></svg></div>
  </div>

  <div class="abs eyebrow">A BIT ABOUT US</div>
  <p class="abs about-text">Backed by years of experience, a trusted nationwide carrier network, and a strong safety-first culture, we provide reliable, adaptable logistics support built around the unique requirements of every load.</p>
  <div class="abs stat" style="left:226px"><b>47%</b><span>Cost Savings</span></div>
  <div class="abs stat" style="left:364px"><b>2.8X</b><span>Delivery Speed</span></div>

  <section class="abs provide"></section>
  <h2 class="abs section-title display" style="left:66px;top:793px">What We Provide</h2>
  <div class="abs arrow-btn" style="left:592px"><svg width="20" height="20"><path d="M14 10H6M9 7L6 10L9 13" stroke="#f3a991" fill="none"/></svg></div>
  <div class="abs arrow-btn on" style="left:619px"><svg width="22" height="22"><path d="M7 11H15M12 8L15 11L12 14" stroke="#fbe3db" fill="none"/></svg></div>

  <article class="abs service-card" style="left:66px">
    <div class="art" role="img" aria-label="Illustration of an orange flatbed truck with cargo"></div>
    <h3 class="display">Flatbed Transportation</h3>
    <p>From routine shipments to oversized and heavy-haul loads, we handle freight requiring proper securement, regulatory knowledge, and consistent on-time execution.</p>
    <div class="tags"><span class="tag">• Safety First</span><span class="tag">• Expert Securement</span><span class="tag">• Cargo Protection</span><span class="tag">• Regulation Complaint</span></div>
  </article>
  <article class="abs service-card light" style="left:360px">
    <div class="art" role="img" aria-label="Illustration of an orange step deck truck"></div>
    <h3 class="display">Step Deck Transportation</h3>
    <p>Our step deck trucking services support tall, heavy, and the most specialized freight that requires additional height clearance and flexible loading options.</p>
    <div class="tags"><span class="tag">• Safety First</span><span class="tag">• Expert Securement</span><span class="tag">• Cargo Protection</span><span class="tag">• Regulation Complaint</span></div>
  </article>
  <article class="abs service-card" style="left:653px">
    <div class="art" role="img" aria-label="Illustration of a dry van truck"></div>
    <h3 class="display">Dry Van Transportation</h3>
    <p>From routine shipments to general freight, we handle freight that needs protection and consistent on-time execution.</p>
    <div class="tags"><span class="tag">• Safety First</span><span class="tag">• Cargo Protection</span></div>
  </article>

  <section class="abs calc"></section>
  <div class="abs calc-art" role="img" aria-label="Illustration of stacked cardboard and orange shipping boxes"></div>
  <h2 class="abs calc-title display">Calculate Your Cost</h2>
  <span class="abs field-label" style="left:127px">Type of Service</span>
  <span class="abs field-label" style="left:281px">Type of Industry</span>
  <span class="abs field-label" style="left:433px">Number of Goods</span>
  <div class="abs select" style="left:127px">Flatbed Transportation<svg width="6" height="4"><path d="M0 0L3 3L6 0" stroke="#8a6a60" fill="none"/></svg></div>
  <div class="abs select" style="left:281px">Pharma &amp; Healthcare<svg width="6" height="4"><path d="M0 0L3 3L6 0" stroke="#8a6a60" fill="none"/></svg></div>
  <div class="abs select" style="left:433px">&lt;50<svg width="6" height="4"><path d="M0 0L3 3L6 0" stroke="#8a6a60" fill="none"/></svg></div>
  <div class="abs calc-btn">Calculate</div>

  <section class="abs why"></section>
  <h2 class="abs section-title display" style="left:66px;top:1590px">Why Choose Us<br>For Your Next Delivery</h2>
  <div class="abs why-list" style="height:200px">
    <div class="why-item" style="top:10px">Industry-compliant food transportation standards</div>
    <div class="why-item" style="top:47px">Experienced carriers familiar with food handling requirements</div>
    <div class="why-item on" style="top:76px">Real-time tracking and reliable delivery timelines<p>Lorem ipsum dolor sit amet, consectetur adipiscing elit, sed do eiusmod tempor incididunt ut labore et dolore magna aliqua. Quis ipsum suspendisse.</p></div>
    <div class="why-item" style="top:121px">Flexible capacity for seasonal demand spikes</div>
    <div class="why-item" style="top:159px">Competitive pricing and scalable logistics solutions</div>
  </div>
  <div class="abs why-photo" role="img" aria-label="Aerial photo of trucks on a desert highway"></div>

  <section class="abs reviews"></section>
  <h2 class="abs section-title display" style="left:66px;top:1953px">What Customers Say</h2>
  <article class="abs review" style="left:66px">
    <svg class="quote" width="18" height="12"><path d="M2 0H8V6L5 12H2L4 6H2Z M10 0H16V6L13 12H10L12 6H10Z" fill="#e85e30"/></svg>
    <div class="avatar" role="img" aria-label="Customer portrait"></div>
    <p>We've worked with several logistics providers before, but Tvar Freight stands out for their efficiency and attention to detail.</p>
    <small>Pell Aronsen, Director of Supply Chain</small>
  </article>
  <article class="abs review" style="left:261px">
    <svg class="quote" width="18" height="12"><path d="M2 0H8V6L5 12H2L4 6H2Z M10 0H16V6L13 12H10L12 6H10Z" fill="#e85e30"/></svg>
    <div class="avatar" role="img" aria-label="Customer portrait"></div>
    <p>We've worked with several logistics providers before, but Tvar Freight stands out for their efficiency and attention to detail.</p>
    <small>Pell Aronsen, Director of Supply Chain</small>
  </article>
  <article class="abs review" style="left:455px">
    <svg class="quote" width="18" height="12"><path d="M2 0H8V6L5 12H2L4 6H2Z M10 0H16V6L13 12H10L12 6H10Z" fill="#e85e30"/></svg>
    <div class="avatar" role="img" aria-label="Customer portrait"></div>
    <p>We've worked with several logistics providers before, but Tvar Freight stands out for their efficiency and attention to detail.</p>
    <small>Pell Aronsen, Director of Supply Chain</small>
  </article>

  <h2 class="abs faq-title display">From The FAQs</h2>
  <div class="abs faq open" style="top:2313px;height:95px">
    <h4>How do you ensure the safety of my cargo?</h4>
    <div class="toggle"><svg width="15" height="15"><path d="M4.5 9L7.5 6L10.5 9" stroke="#2f1209" fill="none"/></svg></div>
    <p class="answer">Lorem ipsum dolor sit amet, consectetur adipiscing elit, sed do eiusmod tempor incididunt ut ror labore et dolore magna aliqua. Quis ipsum suspendisse ultrices gravida. Risus commodo viverra et maecenas accumsan lacus vel facilisis.</p>
  </div>
  <div class="abs faq" style="top:2409px;height:41px"><h4>Do you operate nationwide?</h4><div class="toggle"><svg width="15" height="15"><path d="M4.5 6L7.5 9L10.5 6" stroke="#2f1209" fill="none"/></svg></div></div>
  <div class="abs faq" style="top:2450px;height:41px"><h4>Can you accommodate specialized shipping requirements?</h4><div class="toggle"><svg width="15" height="15"><path d="M4.5 6L7.5 9L10.5 6" stroke="#2f1209" fill="none"/></svg></div></div>
  <div class="abs faq" style="top:2491px;height:41px"><h4>What are your delivery timeframes?</h4><div class="toggle"><svg width="15" height="15"><path d="M4.5 6L7.5 9L10.5 6" stroke="#2f1209" fill="none"/></svg></div></div>
  <div class="abs faq" style="top:2532px;height:41px"><h4>Do you offer real-time updates on my cargo?</h4><div class="toggle"><svg width="15" height="15"><path d="M4.5 6L7.5 9L10.5 6" stroke="#2f1209" fill="none"/></svg></div></div>
  <p class="abs faq-more">Have more questions? Read all faqs here</p>

  <section class="abs cta">
    <h2 class="display">Partner With Tvar Freight To<br>Streamline Your Supply<br>Chain And More</h2>
    <span class="btn">Request a Quote</span>
    <span class="btn ghost">Explore Solutions</span>
  </section>
  <div class="abs cta-art" role="img" aria-label="Illustration of an orange box truck with stacked parcels"></div>

  <p class="abs footer-blurb">We focus on safety and on-time delivery to keep your operations running smoothly.</p>
  <div class="abs footer-contact">sales@tvarfreightglobal.com<br>2025550148</div>
  <div class="abs footer-col" style="left:397px"><h5>Company</h5>About<br>Contact</div>
  <div class="abs footer-col" style="left:464px"><h5>Services</h5>Flatbed Transportation<br>Step Deck Transportation<br>Dry Van Transportation<br>Heavy Haul Transportation</div>
  <div class="abs footer-col" style="left:577px"><h5>Industries</h5>E-Commerce &amp; Retail<br>Food &amp; Beverage<br>Healthcare &amp; Pharma<br>Government<br>Manufacturing</div>
  <p class="abs copyright">© 2026. An independent agent of Halden Group LLC.</p>
</main>
</body>
</html>
```